Fatigued and Overloaded by COVID Messages? We need original illustrations to show that.

Everywhere you look there are messages about COVID. That is leading many people to feel fatigued and overloaded by the messages.

We surveyed U.S. adults March 20th - 24th, 2020 and measured message fatigue, information overload, perceived repetition, and perceived exaggeration. Here is how participants responded:

When it comes to coronavirus . . .
55% feel exhausted by all the messages.
54% feel overloaded by the amount of information.
51% feel that the messages are repetitive.
47% feel like messages exaggerate how bad it is.

In other words, almost half of U.S. adults show signs of message fatigue, information overload, perceived message repetition, and perceived message exaggeration.

We will continue to survey 400 adults every week for the next 16 weeks. Each time we will measure message fatigue, information overload, perceived repetition, and perceived exaggeration. We expect that it will increase over time.

What are we looking for? We need innovative and original illustrations that attempt to communicate these findings. The illustrations would visualize message fatigue, information overload, perceived message repetition, and perceived message exaggeration.

What sort of visual are we looking for? Our preference is for an original illustration (or set of illustrations). Our preference is for creative and powerful illustrations, but we are also open to the creative and well-executed infographics.

We need these images fast . We will award monetary prizes to the 3 best designs. If we like more than that, then we might purchase more (e.g., in past contests, we have purchased as many as 30 designs).

What we will need:
(1) The illustrations must be original and we will need the photoshop and/or illustrator files for all artwork. (By original, we mean that the illustrations are 100% created by you. Our organization requires that we utilize only original illustrated work. We have had issues with free imagery being pirated and reposted as free. We sidestep that issue by just having everything created.)

(2) The illustration should say, somewhere: "Based on a survey of 400 U.S. adults conducted March 20 - 24th, 2020."

(3) We will have almost 4 months worth of data by the time this is done. In other words, the illustrations might be able to help us present that weekly data.

(4) We have conducted other Artvendo projects. It might be helpful to examine designs we liked in the past. For example, here is another COVID project we just finished:

https://jobs.artvendo-example.com/job/5162048

Target Market(s)

U.S. adults

Requirements
Must have
• Original illustrations. Mobile friendly design. People will view this on their smartphones.
Nice to have
• A design that we can use to communicate the data across time.

```html
<!DOCTYPE html>
<html lang="en">
<head>
<meta charset="utf-8">
<title>Fatigued and Overloaded by COVID Messages?</title>
<link rel="stylesheet" href="https://fonts.googleapis.com/css2?family=Catamaran:wght@600;700;800&family=Jost:wght@400&display=swap">
<style>
  :root {
    --page: #ffffff;
    --wall-top: #8fc6aa;
    --wall-right: #6fb28e;
    --wall-low: #9ecfb6;
    --floor: #8bd4a8;
    --skirting: #4e8c66;
    --ink-green: #1d5a32;
    --footer-green: #2b5a3a;
    --panel-teal: #3d746a;
    --panel-charcoal: #4a4646;
    --bar-fill: #ea733a;
    --bar-track: #f3ce6a;
    --blind-dark: #0a5229;
    --blind-light: #4e8a64;
    --blind-slat: #f3ce6a;
    --white: #ffffff;
  }
  * { box-sizing: border-box; margin: 0; padding: 0; }
  html, body { width: 1200px; height: 1200px; overflow: hidden; background: var(--page); }
  .canvas { position: relative; width: 1200px; height: 1200px; }
  .poster {
    position: absolute; left: 184px; top: 44px; width: 839px; height: 1118px;
    background: linear-gradient(135deg, var(--wall-top) 0%, var(--wall-low) 55%, var(--wall-right) 100%);
    overflow: hidden;
    font-family: "Catamaran", sans-serif;
  }
  .skirting { position: absolute; left: 0; right: 0; top: 809px; height: 24px; background: var(--skirting); }
  .floor { position: absolute; left: 0; right: 0; top: 833px; bottom: 0; background: var(--floor); }
  .blind {
    position: absolute; left: 0; top: 87px; width: 100px; height: 372px;
    background: linear-gradient(180deg, var(--blind-dark), var(--blind-light));
  }
  .blind .slat { position: absolute; left: 0; width: 83px; height: 19px; background: var(--blind-slat); }
  .rug {
    position: absolute; left: 347px; top: 856px; width: 492px; height: 220px;
    background: linear-gradient(160deg, #fcf59a 0%, #f7c404 30%, #f7c404 100%);
    clip-path: polygon(20% 0, 100% 0, 100% 100%, 0 92%);
  }
  .figure {
    position: absolute; left: 16px; top: 320px; width: 500px; height: 720px;
    background: linear-gradient(170deg, #6b5e4f 0%, #efd699 22%, #06345c 45%, #2f7285 75%, #d4d5d9 100%);
    clip-path: polygon(19% 0, 100% 0, 100% 100%, 0 100%, 0 20%, 19% 20%);
  }
  .title {
    position: absolute; right: 37px; top: 40px; text-align: right; white-space: nowrap;
    color: var(--white); font-weight: 800; font-size: 60px; line-height: 77px; letter-spacing: -0.8px;
  }
  .intro {
    position: absolute; right: 37px; top: 201px; text-align: right; white-space: nowrap;
    color: var(--ink-green); font-weight: 700; font-size: 19.5px; line-height: 28px;
  }
  .stat {
    position: absolute; left: 422px; width: 417px; height: 87px;
    border-radius: 8px 0 0 8px; text-align: center; color: var(--white);
  }
  .stat--teal { background: var(--panel-teal); }
  .stat--charcoal { background: var(--panel-charcoal); }
  .stat__label { position: absolute; left: 0; right: 0; top: 9px; font-weight: 700; font-size: 18.6px; line-height: 24px; white-space: nowrap; }
  .stat__track {
    position: absolute; left: 37px; top: 44px; width: 342px; height: 29px;
    border-radius: 14px; background: var(--bar-track); overflow: hidden;
  }
  .stat__fill {
    height: 100%; background: var(--bar-fill); text-align: right; padding-right: 6px;
    font-weight: 800; font-size: 21px; line-height: 31px; color: var(--white);
  }
  .summary {
    position: absolute; right: 23px; top: 707px; text-align: right; white-space: nowrap;
    color: #f2f8f3; font-weight: 700; font-size: 15px; line-height: 19px;
  }
  .credit {
    position: absolute; left: 0; right: 0; top: 1074px; text-align: center;
    font-family: "Jost", sans-serif; font-size: 19px; color: var(--footer-green);
  }
</style>
</head>
<body>
<div class="canvas">
  <section class="poster">
    <div class="skirting"></div>
    <div class="floor"></div>

    <div class="blind">
      <div class="slat" style="top:24px"></div>
      <div class="slat" style="top:62px"></div>
      <div class="slat" style="top:100px"></div>
      <div class="slat" style="top:138px;opacity:.95"></div>
      <div class="slat" style="top:176px;opacity:.9"></div>
      <div class="slat" style="top:214px;opacity:.8"></div>
      <div class="slat" style="top:252px;opacity:.7"></div>
      <div class="slat" style="top:290px;opacity:.6"></div>
      <div class="slat" style="top:328px;opacity:.5"></div>
    </div>

    <div class="rug" role="img" aria-label="Illustration of a yellow rug on the floor"></div>
    <div class="figure" role="img" aria-label="Illustration of a tired bearded man on a white beanbag holding his head while reading COVID-19 messages on a phone, with virus particles floating from the screen"></div>

    <h1 class="title">Fatigued and Overloaded<br>by COVID Messages?</h1>

    <p class="intro">We surveyed U.S. adults March 20th - 24th, 2020<br>and measured message fatigue, information overload, perceived repetition,<br>and perceived exaggeration.&nbsp; Here is how participants responded:</p>

    <div class="stat stat--teal" style="top:310px">
      <div class="stat__label">Feel exhausted by all the messages</div>
      <div class="stat__track"><div class="stat__fill" style="width:56%">55%</div></div>
    </div>
    <div class="stat stat--charcoal" style="top:408px">
      <div class="stat__label">Feel overloaded by the amount of information</div>
      <div class="stat__track"><div class="stat__fill" style="width:54%">54%</div></div>
    </div>
    <div class="stat stat--teal" style="top:506px">
      <div class="stat__label">Feel that the messages are repetitive</div>
      <div class="stat__track"><div class="stat__fill" style="width:50%">51%</div></div>
    </div>
    <div class="stat stat--charcoal" style="top:604px">
      <div class="stat__label">Feel like messages exaggerate how bad it is</div>
      <div class="stat__track"><div class="stat__fill" style="width:47%">47%</div></div>
    </div>

    <p class="summary">In other words, almost half of U.S. adults<br>show signs of message fatigue, information<br>overload, perceived message repetition,<br>and perceived message exaggeration.</p>

    <p class="credit">Based on a survey of 400 U.S. adults conducted March 20 - 24th, 2020</p>
  </section>
</div>
</body>
</html>
```